New locally owned rental company needs a flyer to circulate

Need flyer with logo, phone# and address. We rent cars to anyone with driver's license and proper insurance. Rates as low as $50/day. Can offer compact cars, mid-size and full size sedans. Also SUV's.

```html
<!DOCTYPE html>
<html lang="en">
<head>
<meta charset="UTF-8">
<title>DriveSoon Car &amp; Van Rental Flyer</title>
<link rel="stylesheet" href="https://fonts.googleapis.com/css2?family=Roboto+Condensed:wght@700;800&family=Open+Sans:ital,wght@1,600&family=Arimo:wght@400;700&display=swap">
<style>
  :root {
    --brand-blue: #0a4fa0;
    --brand-green: #1aab4a;
    --ink: #231f20;
    --white: #ffffff;
    --sky-top: #cdcac3;
    --sky-mid: #e2dccf;
    --sunset: #e9b488;
    --haze: #8d9299;
    --field: #4a555c;
    --road: #2b3238;
    --car-body: #6f8a92;
    --car-shade: #3f5158;
  }
  * { margin: 0; padding: 0; box-sizing: border-box; }
  html, body {
    width: 848px;
    height: 1200px;
    overflow: hidden;
    background: var(--brand-blue);
  }
  .flyer {
    position: relative;
    width: 848px;
    height: 1200px;
    overflow: hidden;
  }
  .landscape-photo {
    position: absolute;
    inset: 0;
    background: linear-gradient(180deg,
      var(--sky-top) 0%,
      var(--sky-mid) 36%,
      var(--sunset) 46%,
      #c9a58e 50%,
      var(--haze) 56%,
      var(--field) 68%,
      var(--road) 100%);
  }
  .car-photo {
    position: absolute;
    left: 22px;
    top: 640px;
    width: 800px;
    height: 410px;
    border-radius: 44% 48% 18% 18% / 40% 44% 14% 14%;
    background: radial-gradient(ellipse at 55% 45%,
      var(--car-body) 0%,
      #587078 45%,
      var(--car-shade) 75%,
      rgba(63, 81, 88, 0) 100%);
  }
  .brand {
    position: absolute;
    top: 50px;
    left: 0;
    width: 100%;
    text-align: center;
  }
  .brand-name {
    font-family: "Roboto Condensed", sans-serif;
    font-weight: 800;
    font-size: 38px;
    line-height: 1;
    color: var(--brand-blue);
  }
  .brand-tagline {
    margin-top: 6px;
    font-family: "Arimo", sans-serif;
    font-weight: 700;
    font-size: 13px;
    letter-spacing: 5px;
    color: var(--ink);
  }
  .headline {
    position: absolute;
    left: 46px;
    top: 168px;
    font-family: "Roboto Condensed", sans-serif;
    font-weight: 800;
    font-size: 96px;
    line-height: 86px;
    letter-spacing: -1px;
    color: var(--ink);
    text-transform: uppercase;
  }
  .headline .accent { color: var(--brand-blue); }
  .price-badge {
    position: absolute;
    left: 482px;
    top: 250px;
    width: 314px;
    height: 158px;
    border-radius: 18px;
    background: var(--brand-blue);
    color: var(--white);
    text-align: center;
  }
  .price-label {
    margin: 22px 22px 0;
    padding-bottom: 8px;
    border-bottom: 2px solid var(--white);
    font-family: "Arimo", sans-serif;
    font-weight: 700;
    font-size: 21px;
  }
  .price-value {
    margin-top: 4px;
    font-family: "Roboto Condensed", sans-serif;
    font-weight: 800;
    font-size: 74px;
    line-height: 84px;
  }
  .requirements {
    position: absolute;
    left: 48px;
    top: 440px;
    font-family: "Open Sans", sans-serif;
    font-style: italic;
    font-weight: 600;
    font-size: 34px;
    line-height: 40px;
    letter-spacing: -0.5px;
    color: var(--ink);
  }
  .fleet-band {
    position: absolute;
    left: 0;
    top: 549px;
    width: 655px;
    height: 67px;
    background: var(--brand-green);
    display: flex;
    align-items: center;
    padding-left: 45px;
    font-family: "Roboto Condensed", sans-serif;
    font-weight: 700;
    font-size: 29px;
    color: var(--white);
    text-transform: uppercase;
  }
  .contact-bar {
    position: absolute;
    left: 0;
    bottom: 0;
    width: 100%;
    height: 77px;
    background: var(--brand-blue);
    color: var(--white);
    font-family: "Arimo", sans-serif;
    font-size: 21px;
  }
  .contact-item {
    position: absolute;
    top: 0;
    height: 77px;
    display: flex;
    align-items: center;
    gap: 6px;
  }
  .contact-phone { left: 72px; }
  .contact-address { left: 328px; gap: 12px; }
  .contact-item svg { fill: var(--white); }
</style>
</head>
<body>
  <main class="flyer">
    <div class="landscape-photo" role="img" aria-label="Sunset sky over misty hills, fields and a dark road"></div>
    <div class="car-photo" role="img" aria-label="Grey sports coupe parked on the road, front three-quarter view"></div>

    <header class="brand">
      <div class="brand-name">DriveSoon</div>
      <div class="brand-tagline">Car &amp; Van Rental</div>
    </header>

    <h1 class="headline">Best Car<br>For <span class="accent">Rent</span><br>Today!</h1>

    <div class="price-badge">
      <div class="price-label">PRICE STARTING FROM</div>
      <div class="price-value">$50/DAY</div>
    </div>

    <p class="requirements">With driver's license<br>and proper insurance.</p>

    <div class="fleet-band">Compact Cars | Mid-Size | Full Size Sedans</div>

    <footer class="contact-bar">
      <div class="contact-item contact-phone">
        <svg width="22" height="22" viewBox="0 0 24 24" aria-hidden="true"><path d="M6.6 10.8a15.1 15.1 0 0 0 6.6 6.6l2.2-2.2a1 1 0 0 1 1-.25 11.4 11.4 0 0 0 3.6.57 1 1 0 0 1 1 1V20a1 1 0 0 1-1 1A17 17 0 0 1 3 4a1 1 0 0 1 1-1h3.5a1 1 0 0 1 1 1c0 1.25.2 2.45.57 3.57a1 1 0 0 1-.25 1z"/></svg>
        <span>+1 555 014 288</span>
      </div>
      <div class="contact-item contact-address">
        <svg width="18" height="24" viewBox="0 0 18 24" aria-hidden="true"><path d="M9 0a9 9 0 0 0-9 9c0 6.8 9 15 9 15s9-8.2 9-15a9 9 0 0 0-9-9zm0 12.5A3.5 3.5 0 1 1 9 5.5a3.5 3.5 0 0 1 0 7z"/></svg>
        <span>48 Harbor Lane, Suite 2, Millbrook</span>
      </div>
    </footer>
  </main>
</body>
</html>
```